rt for guide - bartholomew finch personal speaking/consulting website

custom website for my personal speaking/consulting services brand, you can see the basic site we are using as a placeholder at www.rtforguide.example now. I want to re-position this to more of a personal brand site and have video samples of speaking events, downloadable content, a video blog, and links to podcast. I really like the design of dorianwelk.example and the feature set should be fairly similar to his. I'll begin to compile more stock images etc. to use for sliders like he has done, for now we'll need to use stock imagery or existing photography from my social accounts. You can get a feel for social at all platforms/bfinchbroker i.e. facebook.com/bfinchbroker. the site should be primarily geared toward showcasing speaking/consulting services and content, as well as be flexible to allow for additional downloadables etc. in the future.

Target Market(s)

entrepreneurs and leaders looking to grow themselves, their business, and those they lead.

Coding

Coded - Design and coding required

Number of Pages Required

3 page

Font styles to use
Sans Serif

Colors

Designer to choose colors to be used in the design.

Requirements
Must have
• modern slick design, video blog, podcast feed, registration for people to subscribe to newsletter

```html
<!DOCTYPE html>
<html lang="en">
<head>
<meta charset="utf-8">
<title>RT for Guide — Bartholomew Finch</title>
<link href="https://fonts.googleapis.com/css2?family=Montserrat:wght@400;500;600;700&family=Lato:wght@300;400;700&display=swap" rel="stylesheet">
<style>
:root{
  --orange:#f26b2a;
  --orange-light:#f7874b;
  --ink:#1d1d1f;
  --body:#5a5a5a;
  --muted:#8a8a8a;
  --panel:#f4f4f4;
  --field:#ececec;
  --dark:#2a2730;
  --footer:#181818;
  --footer-bar:#0d0d0d;
  --white:#ffffff;
}
*{box-sizing:border-box;margin:0;padding:0}
html,body{width:1200px;height:4875px;overflow:hidden}
body{font-family:'Lato',sans-serif;color:var(--body);background:var(--white);position:relative}
.abs{position:absolute}
h1,h2,h3,.logo,.btn{font-family:'Montserrat',sans-serif}

/* header + hero */
.hero{position:absolute;left:0;top:0;width:1200px;height:636px;
  background:radial-gradient(ellipse at 50% 60%,#4a4550 0%,#33303a 45%,#22202a 100%)}
.site-header{position:absolute;left:0;top:0;width:1200px;height:95px;border-bottom:1px solid rgba(255,255,255,.08)}
.logo{position:absolute;left:78px;top:28px;font-size:30px;font-weight:600;color:var(--white);letter-spacing:.5px}
.main-nav{position:absolute;left:343px;top:37px;display:flex;gap:26px;font-size:14px;color:var(--white);text-transform:uppercase}
.main-nav .active{color:var(--orange)}
.btn{display:flex;align-items:center;justify-content:center;background:var(--orange);color:var(--white);
  font-size:15px;font-weight:600;letter-spacing:1.2px;text-transform:uppercase}
.header-cta{left:956px;top:25px;width:167px;height:45px}
.hero-title{position:absolute;left:0;width:1200px;top:240px;text-align:center;color:var(--white);
  font-size:92px;font-weight:600;letter-spacing:3px}
.hero-rule{left:255px;top:384px;width:688px;height:1px;background:rgba(255,255,255,.6)}
.hero-text{left:255px;top:420px;width:690px;text-align:center;color:#e8e8e8;font-size:15px;line-height:27px}

/* signup band */
.signup{left:0;top:636px;width:1200px;height:311px;background:var(--orange);overflow:hidden}
.signup h2{position:absolute;top:58px;width:1200px;text-align:center;color:var(--white);font-size:31px;font-weight:600}
.signup p{position:absolute;top:120px;width:1200px;text-align:center;color:var(--white);font-size:17px}
.field-line{height:51px;border:1px solid rgba(255,255,255,.85);color:var(--white);font-size:13px;padding:18px 16px}
.signup .btn-light{background:var(--white);color:var(--orange)}

/* welcome */
.welcome h2{left:78px;top:1070px;font-size:38px;font-weight:600;color:var(--ink)}
.lead{left:78px;top:1136px;width:500px;font-size:17px;line-height:29px;color:#555}
.small-copy{left:78px;top:1244px;width:500px;font-size:13px;line-height:25px;color:#6a6a6a}
.read-more{left:78px;top:1397px;width:187px;height:51px}
.photo{display:block}

/* dark patterned sections */
.pattern-band{left:0;width:1200px;
  background:linear-gradient(135deg,#6b5a3f 0%,#3b2a26 22%,#7a3522 45%,#2c2226 65%,#8a4424 85%,#3a2c2a 100%)}
.band-title{position:absolute;left:0;width:1200px;text-align:center;color:var(--white);font-size:38px;font-weight:600}
.event-card{background:var(--white)}
.event-caption{position:absolute;left:18px;top:16px;width:228px;font-size:13px;line-height:25px;color:#777}
.event-arrow{position:absolute;right:16px;top:26px}

/* downloads */
.section-title{position:absolute;left:0;width:1200px;text-align:center;color:var(--ink);font-size:38px;font-weight:600}
.download{left:78px;width:1045px;height:226px;background:var(--panel)}
.dl-thumb{position:absolute;left:45px;top:50px;width:125px;height:125px;border-radius:50%}
.dl-kicker{position:absolute;left:229px;top:52px;font-size:15px;color:#6a6a6a}
.dl-title{position:absolute;left:229px;top:92px;font-family:'Montserrat',sans-serif;font-size:27px;font-weight:600;color:var(--ink)}
.dl-link{position:absolute;left:229px;top:146px;font-size:15px;color:var(--orange)}
.dl-icon{position:absolute;left:920px;top:71px}

.podcast{left:0;top:3616px;width:1200px;height:394px;background:radial-gradient(ellipse at 50% 50%,#45414b 0%,#2b2830 70%)}
.podcast h2{position:absolute;top:199px;width:1200px;text-align:center;color:var(--white);font-size:38px;font-weight:500}
.podcast p{position:absolute;left:340px;top:268px;width:520px;text-align:center;color:#e2e2e2;font-size:16px;line-height:28px}

.input{background:var(--field);color:#777;font-size:14px;padding:14px 20px}

.site-footer{left:0;top:4460px;width:1200px;height:358px;background:var(--footer)}
.footer-logo{position:absolute;top:70px;width:1200px;text-align:center;font-family:'Montserrat',sans-serif;font-size:44px;font-weight:600;color:var(--white)}
.social{position:absolute;top:166px;width:61px;height:61px;background:#2a2a2a;border:1px solid #333}
.social.active{background:var(--orange);border-color:var(--orange)}
.footer-nav{position:absolute;top:278px;width:1200px;display:flex;justify-content:center;gap:24px;font-size:14px;color:var(--white)}
.footer-nav span.sep{color:#aaa}
.legal{left:0;top:4818px;width:1200px;height:57px;background:var(--footer-bar);color:#cfcfcf;font-size:13px;text-align:center;line-height:57px}
</style>
</head>
<body>

<section class="hero" role="img" aria-label="Audience seated at a speaking event, darkened">
  <header class="site-header">
    <div class="logo">RT for Guide</div>
    <nav class="main-nav"><span class="active">Home</span><span>About</span><span>Video Blog</span><span>Podcast</span><span>Events</span><span>Contact</span></nav>
    <div class="btn abs header-cta">Contact</div>
  </header>
  <h1 class="hero-title">LOREM IPSUM</h1>
  <div class="abs hero-rule"></div>
  <p class="abs hero-text">Lorem Ipsum is simply dummy text of the printing and typesetting industry. Lorem Ipsum has been the industry's standard dummy text ever since the 1500s, when an unknown printer.</p>
</section>

<section class="abs signup">
  <svg class="abs" style="left:0;top:0" width="1200" height="311"><polygon points="520,311 1200,170 1200,311" fill="#f47a3c"/></svg>
  <h2>Make a FULL TIME LIVING doing what you love!</h2>
  <p>SIGN UP TO LEARN THESE simple steps.</p>
  <div class="abs field-line" style="left:255px;top:178px;width:250px">Name</div>
  <div class="abs field-line" style="left:517px;top:178px;width:250px">Email</div>
  <div class="abs btn btn-light" style="left:778px;top:178px;width:165px;height:51px">Contact</div>
</section>

<section class="welcome">
  <h2 class="abs">Welcome to RT for Guide</h2>
  <p class="abs lead">Lorem Ipsum is simply dummy text of the printing and typesetting industry. Lorem Ipsum has been the industry's standard dummy text ever.</p>
  <p class="abs small-copy">It has survived not only five centuries, but also the leap into electronic typesetting, remaining essentially unchanged. It was popularised in the 1960s with the release of Sheetline sheets containing Lorem Ipsum passages, and more recently with desktop publishing software like Quillpage Composer including versions of Lorem Ipsum.</p>
  <div class="abs btn read-more">Read More</div>
  <div class="abs photo" style="left:789px;top:1041px;width:334px;height:417px;background:linear-gradient(180deg,#e9e9e9 0%,#9a8f88 45%,#5a4a44 70%,#d8c29a 100%)" role="img" aria-label="Audience listening to a speaker on stage"></div>
  <div class="abs" style="left:712px;top:1255px;width:238px;height:239px;background:#ededed"></div>
  <div class="abs photo" style="left:727px;top:1272px;width:208px;height:206px;background:linear-gradient(180deg,#f3f3f3 0%,#c9a88e 50%,#2f3a55 100%)" role="img" aria-label="Portrait of Bartholomew Finch"></div>
</section>

<section class="abs pattern-band" style="top:1583px;height:552px" role="img" aria-label="Dark faceted polygon background">
  <h2 class="band-title" style="top:66px">Speaking Events</h2>
  <div class="abs event-card" style="left:78px;top:143px;width:331px;height:311px">
    <div style="height:229px;background:linear-gradient(135deg,#7fa35a,#d9b89a 55%,#c8a070)" role="img" aria-label="Guests with face paint at an event"></div>
    <div style="position:relative"><p class="event-caption">Lorem Ipsum is simply dummy text of the printing and typesetting.</p>
    <svg class="event-arrow" width="30" height="30"><circle cx="15" cy="15" r="15" fill="#f26b2a"/><path d="M8 15h13M16 10l5 5-5 5" stroke="#fff" stroke-width="2.4" fill="none"/></svg></div>
  </div>
  <div class="abs event-card" style="left:433px;top:143px;width:332px;height:311px">
    <div style="height:229px;background:linear-gradient(180deg,#4a5a78 0%,#d9a25a 45%,#3c3f48 75%,#5b5b5b)" role="img" aria-label="Harbour at sunset with boats"></div>
    <div style="position:relative"><p class="event-caption">Lorem Ipsum is simply dummy text of the printing and typesetting.</p>
    <svg class="event-arrow" width="30" height="30"><circle cx="15" cy="15" r="15" fill="#f26b2a"/><path d="M8 15h13M16 10l5 5-5 5" stroke="#fff" stroke-width="2.4" fill="none"/></svg></div>
  </div>
  <div class="abs event-card" style="left:789px;top:143px;width:334px;height:311px">
    <div style="height:229px;background:linear-gradient(180deg,#dfe6ee 0%,#9fb0c2 50%,#4d5a66 80%,#8aa06a)" role="img" aria-label="Inflatable display at a waterfront event"></div>
    <div style="position:relative"><p class="event-caption">Lorem Ipsum is simply dummy text of the printing and typesetting.</p>
    <svg class="event-arrow" width="30" height="30"><circle cx="15" cy="15" r="15" fill="#f26b2a"/><path d="M8 15h13M16 10l5 5-5 5" stroke="#fff" stroke-width="2.4" fill="none"/></svg></div>
  </div>
</section>

<section class="downloads">
  <h2 class="section-title" style="top:2193px">Downloadable Content</h2>
  <div class="abs download" style="top:2281px">
    <div class="dl-thumb" style="background:radial-gradient(circle,#f4e4d0,#b0684a)" role="img" aria-label="Bright window light scene"></div>
    <p class="dl-kicker">Lorem Ipsum is simply dummy text.</p>
    <h3 class="dl-title">It has survived not only five centuries.</h3>
    <p class="dl-link">Lorem Ipsum is simply.</p>
    <svg class="dl-icon" width="84" height="84"><circle cx="42" cy="42" r="41" fill="#fff" stroke="#ddd" stroke-width="1.5"/><path d="M42 30v18M35 41l7 7 7-7M31 46v8h22v-8" stroke="#f26b2a" stroke-width="2.2" fill="none"/></svg>
  </div>
  <div class="abs download" style="top:2540px">
    <div class="dl-thumb" style="background:radial-gradient(circle at 50% 30%,#e08a4a,#2a2f55 70%)" role="img" aria-label="Crowd at a conference hall"></div>
    <p class="dl-kicker">Lorem Ipsum is simply dummy text.</p>
    <h3 class="dl-title">It has survived not only five centuries.</h3>
    <p class="dl-link">Lorem Ipsum is simply.</p>
    <svg class="dl-icon" width="84" height="84"><circle cx="42" cy="42" r="41" fill="#fff" stroke="#ddd" stroke-width="1.5"/><path d="M42 30v18M35 41l7 7 7-7M31 46v8h22v-8" stroke="#f26b2a" stroke-width="2.2" fill="none"/></svg>
  </div>
  <div class="abs download" style="top:2802px">
    <div class="dl-thumb" style="background:linear-gradient(180deg,#cfe0ee,#8aa0b5 60%,#3a3a3a)" role="img" aria-label="Rock tower against the sky"></div>
    <p class="dl-kicker">Lorem Ipsum is simply dummy text.</p>
    <h3 class="dl-title">It has survived not only five centuries.</h3>
    <p class="dl-link">Lorem Ipsum is simply.</p>
    <svg class="dl-icon" width="84" height="84"><circle cx="42" cy="42" r="41" fill="#fff" stroke="#ddd" stroke-width="1.5"/><path d="M42 30v18M35 41l7 7 7-7M31 46v8h22v-8" stroke="#f26b2a" stroke-width="2.2" fill="none"/></svg>
  </div>
  <div class="abs btn" style="left:505px;top:3057px;width:188px;height:51px">Explore More</div>
</section>

<section class="abs pattern-band" style="top:3199px;height:417px" role="img" aria-label="Dark faceted polygon background">
  <h2 class="band-title" style="top:60px">Video Blog</h2>
  <div class="abs" style="left:78px;top:137px;width:187px;height:187px;background:linear-gradient(180deg,#eeeeee,#c9c9c9 55%,#2a3140)" role="img" aria-label="Video still of the speaker in a suit"></div>
  <div class="abs" style="left:292px;top:137px;width:187px;height:187px;background:linear-gradient(135deg,#f07a3a 0%,#f07a3a 45%,#d9d2cc 46%,#b9b0aa)" role="img" aria-label="Video still of the speaker, play button">
    <svg class="abs" style="left:67px;top:67px" width="52" height="52"><circle cx="26" cy="26" r="23" fill="none" stroke="#111" stroke-width="4"/><polygon points="21,15 21,37 38,26" fill="#111"/></svg>
  </div>
  <div class="abs" style="left:507px;top:137px;width:187px;height:187px;background:linear-gradient(180deg,#f2f2f2,#cfd3d8 45%,#2e55a8)" role="img" aria-label="Video still of the speaker in blue shirt"></div>
  <div class="abs" style="left:721px;top:137px;width:187px;height:187px;background:linear-gradient(180deg,#f4f4f4,#d4c0b0 45%,#d02a2a)" role="img" aria-label="Video still of the speaker in red shirt"></div>
  <div class="abs" style="left:935px;top:137px;width:188px;height:187px;background:linear-gradient(180deg,#cfcfcf,#b89c86 45%,#1d1d1d)" role="img" aria-label="Video still of the speaker in dark shirt"></div>
</section>

<section class="abs podcast" role="img" aria-label="Darkened audience background">
  <svg class="abs" style="left:562px;top:92px" width="76" height="76"><circle cx="38" cy="38" r="37" fill="#f26b2a"/><polygon points="31,25 31,51 52,38" fill="#fff"/></svg>
  <h2>Podcast Feed</h2>
  <p>Lorem Ipsum is simply dummy text of the printing and typesetting industry. Lorem Ipsum has been the industry's standard.</p>
</section>

<section class="contact">
  <h2 class="section-title" style="top:4066px;font-weight:500">Get In Touch</h2>
  <div class="abs input" style="left:193px;top:4140px;width:261px;height:45px">Name</div>
  <div class="abs input" style="left:469px;top:4140px;width:262px;height:45px">Email</div>
  <div class="abs input" style="left:746px;top:4140px;width:259px;height:45px">Phone</div>
  <div class="abs input" style="left:193px;top:4202px;width:812px;height:104px">Your Question or Message</div>
  <div class="abs btn" style="left:505px;top:4323px;width:188px;height:50px">Explore More</div>
</section>

<footer class="abs site-footer">
  <div class="footer-logo">RT for Guide</div>
  <div class="social" style="left:386px" aria-label="Social link"></div>
  <div class="social" style="left:460px" aria-label="Social link"></div>
  <div class="social active" style="left:534px" aria-label="Social link"></div>
  <div class="social" style="left:608px" aria-label="Social link"></div>
  <div class="social" style="left:682px" aria-label="Social link"></div>
  <div class="social" style="left:753px" aria-label="Social link"></div>
  <nav class="footer-nav"><span>Home</span><span class="sep">|</span><span>About</span><span class="sep">|</span><span>Video Blog</span><span class="sep">|</span><span>Podcast</span><span class="sep">|</span><span>Events</span><span class="sep">|</span><span>Contact</span></nav>
</footer>
<div class="abs legal">©RT for Guide. 2019 · All Rights Reserved.</div>

</body>
</html>
```